New Website Design for Rides for Heroes.org - A Site for People to Donate Cars to War / Disabled Ve

Current site: www.ridesforheroes.org; Look at these sites for ideas: bikez2tots.org; gearsforhopes.org; www.autosformarines.org; www.trucksforsoldiers.org

Industry/Entity Type

Charity

Coding

Coded - Design and coding required

Number of Pages Required

1 page

Requirements
Must have
• n/a
Nice to have
• n/a
Should not have
• n/a

```html
<!DOCTYPE html>
<html lang="en">
<head>
<meta charset="utf-8">
<title>Rides for Heroes – Donate Your Car</title>
<link rel="stylesheet" href="https://fonts.googleapis.com/css2?family=Raleway:wght@400;500;600;700&display=swap">
<style>
:root{
  --blue:#0c6cc4;
  --navy:#123c6a;
  --red:#c0161b;
  --ink:#2b2b2b;
  --grey-card:#e6e6e6;
  --dark:#2a1e14;
  --white:#ffffff;
}
*{margin:0;padding:0;box-sizing:border-box}
html,body{width:938px;height:1200px;overflow:hidden;background:#fff}
body{position:relative;font-family:"Raleway",sans-serif;color:var(--ink)}
.abs{position:absolute}

/* header */
.site-header{position:absolute;left:0;top:0;width:938px;height:72px;background:#fff}
.brand{position:absolute;left:104px;top:25px;display:flex;align-items:center;gap:8px;font-size:17px;font-weight:600;color:var(--red)}
.brand-dot{width:18px;height:18px;border-radius:50%;background:var(--red)}
.header-call{position:absolute;right:104px;top:12px;font-size:15px;color:#222}
.header-call b{font-weight:600}
.btn-donate{position:absolute;left:675px;top:36px;width:158px;height:23px;background:var(--blue);color:#fff;font-size:11px;display:flex;align-items:center;justify-content:center;border-radius:2px}

/* hero */
.hero{position:absolute;left:0;top:72px;width:938px;height:344px;clip-path:polygon(0 0,100% 0,100% 97%,0 100%);
  background:linear-gradient(120deg,#b59c7e 0%,#9a8566 30%,#c4b197 55%,#8c7658 80%,#a89274 100%)}
.feature{position:absolute;width:90px;text-align:center;font-size:9.5px;line-height:10px;color:#222}
.feature .disc{width:60px;height:60px;margin:0 auto 6px;border-radius:50%;background:rgba(255,255,255,.75);border:2px solid #d7a6a6;display:flex;align-items:center;justify-content:center}

.donate-form{position:absolute;left:541px;top:102px;width:292px;height:226px;background:#fff}
.form-head{height:32px;background:#e8ebee;display:flex;align-items:center;justify-content:center;font-size:14px;color:var(--blue)}
.form-head b{font-weight:600;margin-left:4px}
.field{position:absolute;width:133px;height:23px;border:1px solid #c9c9c9;border-radius:2px;font-size:9px;color:#666;padding-left:8px;display:flex;align-items:center}
.btn-help{position:absolute;left:7px;top:178px;width:276px;height:28px;background:var(--blue);color:#fff;font-size:12px;display:flex;align-items:center;justify-content:center;border-radius:2px}
.help-note{position:absolute;left:548px;top:328px;width:276px;height:38px;background:rgba(255,255,255,.55);text-align:center;color:var(--navy);font-size:10px;line-height:11px;padding-top:5px}
.help-note strong{display:block;font-size:14px;font-weight:500;margin-top:1px}

/* steps */
.section-title{position:absolute;left:0;width:938px;text-align:center;font-size:23px;color:var(--blue);font-weight:400}
.section-title b{font-weight:600}
.title-rule{position:absolute;top:454px;height:1px;width:40px;background:#b9cbe0}
.step{position:absolute;top:541px;width:235px;height:129px;background:var(--grey-card);text-align:center}
.step-icon{position:absolute;top:-44px;left:73px;width:88px;height:88px;border-radius:50%;background:#fff;border:1px solid #ddd;display:flex;align-items:center;justify-content:center}
.step h3{position:absolute;top:52px;width:100%;font-size:22px;font-weight:500;color:#222}
.step p{position:absolute;top:82px;width:100%;font-size:11.5px;line-height:15px;color:#333}

/* why */
.why{position:absolute;left:0;top:734px;width:938px;height:386px;background:linear-gradient(180deg,#241a12 0%,#3a2b1c 45%,#6a4c2c 75%,#1a130c 100%)}
.why-title{position:absolute;top:40px;width:100%;text-align:center;color:#fff;font-size:22px;font-weight:400}
.why-title b{font-weight:600}
.reason{position:absolute;width:240px;color:#fff}
.reason h4{font-size:13px;font-weight:500;margin-bottom:4px}
.reason p{font-size:10.2px;line-height:16px;color:#d8d0c6}
.silhouette{position:absolute;left:555px;top:220px;width:180px;height:166px;background:radial-gradient(ellipse at center,#120c07 0%,rgba(18,12,7,0) 70%)}

/* footer */
.site-footer{position:absolute;left:0;top:1120px;width:938px;height:80px;background:#0d0906;color:#fff}
.social{position:absolute;top:31px;left:0;width:100%;display:flex;justify-content:center;gap:16px}
.social span{width:14px;height:14px;border-radius:50%;background:#fff}
.copy{position:absolute;top:55px;width:100%;text-align:center;font-size:9.5px}
</style>
</head>
<body>

<header class="site-header">
  <div class="brand"><span class="brand-dot"></span>Rides for Heroes</div>
  <div class="header-call">CALL: <b>1-800-555-0142</b></div>
  <div class="btn-donate">DONATE NOW</div>
</header>

<section class="hero" role="img" aria-label="Photo of soldiers in desert camouflage uniforms standing in a row"></section>

<div class="feature" style="left:139px;top:282px">
  <div class="disc"><svg width="34" height="34" viewBox="0 0 34 34"><path d="M17 3a10 10 0 0 0-10 10c0 8 10 18 10 18s10-10 10-18A10 10 0 0 0 17 3z" fill="#c0161b"/><circle cx="17" cy="13" r="4" fill="#fff"/></svg></div>
  Donation Accepted Nationwide
</div>
<div class="feature" style="left:230px;top:282px">
  <div class="disc"><svg width="40" height="24" viewBox="0 0 40 24"><path d="M3 15l4-8h22l6 8h2v5H3z" fill="#c0161b"/><circle cx="11" cy="20" r="3.5" fill="#fff" stroke="#c0161b" stroke-width="2"/><circle cx="29" cy="20" r="3.5" fill="#fff" stroke="#c0161b" stroke-width="2"/></svg></div>
  All Vehicle Types Welcome
</div>
<div class="feature" style="left:315px;top:282px">
  <div class="disc"><svg width="34" height="34" viewBox="0 0 34 34"><circle cx="17" cy="20" r="12" fill="#c0161b"/><rect x="13" y="4" width="8" height="5" fill="#c0161b"/><text x="17" y="25" text-anchor="middle" font-size="14" font-weight="700" fill="#fff" font-family="Raleway,sans-serif">$</text></svg></div>
  Tax Deducted
</div>
<div class="feature" style="left:403px;top:282px">
  <div class="disc"><svg width="42" height="24" viewBox="0 0 42 24"><rect x="2" y="12" width="30" height="6" fill="#c0161b"/><path d="M26 4h8l6 8v6h-14z" fill="#c0161b"/><rect x="5" y="6" width="16" height="6" fill="#c0161b"/><circle cx="9" cy="20" r="3" fill="#fff" stroke="#c0161b" stroke-width="2"/><circle cx="33" cy="20" r="3" fill="#fff" stroke="#c0161b" stroke-width="2"/></svg></div>
  Towing is Free
</div>

<form class="donate-form">
  <div class="form-head">CAR <b>DONATION</b></div>
  <div class="field" style="left:7px;top:56px">NAME</div>
  <div class="field" style="left:150px;top:56px">EMAIL</div>
  <div class="field" style="left:7px;top:85px">PHONE NUMBER</div>
  <div class="field" style="left:150px;top:85px">MOBILE</div>
  <div class="field" style="left:7px;top:115px">ADDRESS</div>
  <div class="field" style="left:150px;top:115px">CITY</div>
  <div class="field" style="left:7px;top:145px">STATE
    <svg style="position:absolute;right:8px;top:8px" width="10" height="6" viewBox="0 0 10 6"><path d="M1 1l4 4 4-4" fill="none" stroke="#888" stroke-width="1.2"/></svg></div>
  <div class="field" style="left:150px;top:145px">ZIP CODE</div>
  <div class="btn-help">HELP VETERANS</div>
</form>
<div class="help-note">WE NEED YOUR HELP<strong>CALL: 1-800-555-0142</strong></div>

<span class="title-rule" style="left:272px"></span>
<h2 class="section-title" style="top:440px"><b>DONATE</b> YOUR <b>CAR</b> TODAY!</h2>
<span class="title-rule" style="left:626px"></span>

<div class="step" style="left:103px">
  <div class="step-icon"><svg width="40" height="52" viewBox="0 0 40 52"><rect x="2" y="4" width="36" height="46" rx="2" fill="none" stroke="#c0161b" stroke-width="2.5"/><rect x="13" y="1" width="14" height="6" fill="#c0161b"/><g stroke="#c0161b" stroke-width="2.5"><path d="M9 16h4M17 16h14M9 24h4M17 24h14M9 32h4M17 32h14M17 40h14"/><path d="M8 40l3 3 5-6" fill="none"/></g></svg></div>
  <h3>Fill Out Form</h3>
  <p>or call 1-800-555-0142<br>Relax, we do the rest</p>
</div>
<div class="step" style="left:351px">
  <div class="step-icon"><svg width="70" height="34" viewBox="0 0 70 34"><rect x="2" y="20" width="50" height="7" fill="#c0161b"/><path d="M44 6h12l10 12v9H44z" fill="#c0161b"/><path d="M6 20l4-9h20l6 9z" fill="#c0161b"/><circle cx="13" cy="28" r="4" fill="#fff" stroke="#c0161b" stroke-width="2.5"/><circle cx="55" cy="28" r="4" fill="#fff" stroke="#c0161b" stroke-width="2.5"/></svg></div>
  <h3>Free Towing</h3>
  <p>Running or Not<br>You have no costs</p>
</div>
<div class="step" style="left:599px">
  <div class="step-icon"><svg width="56" height="44" viewBox="0 0 56 44"><circle cx="14" cy="26" r="12" fill="#c0161b"/><circle cx="42" cy="26" r="12" fill="#c0161b"/><circle cx="28" cy="28" r="15" fill="#c0161b" stroke="#fff" stroke-width="2"/><rect x="22" y="6" width="12" height="6" fill="#c0161b"/><text x="28" y="35" text-anchor="middle" font-size="18" font-weight="700" fill="#fff" font-family="Raleway,sans-serif">$</text></svg></div>
  <h3>Tax Deductible</h3>
  <p>We issue you an IRS tax receipt<br>Take care of all paperwork, DMV &amp; Smog</p>
</div>

<section class="why" role="img" aria-label="Sunset backdrop with the silhouette of a veteran in a wheelchair">
  <div class="silhouette"></div>
  <h2 class="why-title">WHY <b>DONATE</b> YOUR <b>CAR</b> TO US?</h2>
  <div class="reason" style="left:102px;top:96px"><h4>TrustMark A+ Rated &amp; IRS 501(c)3 Approved:</h4><p>Free 24/7 Pickup with No DMV Hassles.</p></div>
  <div class="reason" style="left:352px;top:96px"><h4>Free Local Towing:</h4><p>We will pick up your car donation, running or not, when it's most convenient, at home or work.</p></div>
  <div class="reason" style="left:599px;top:96px"><h4>All Cars Accepted:</h4><p>We take your car regardless of its condition or registration status.</p></div>
  <div class="reason" style="left:102px;top:177px"><h4>Income Tax Deduction:</h4><p>We issue you an IRS tax receipt &amp; offer the largest resale network to get you the highest tax</p></div>
  <div class="reason" style="left:352px;top:177px"><h4>No Paperwork Hassles:</h4><p>We take any car and handle everything: DMV, Smog and IRS paperwork.</p></div>
  <div class="reason" style="left:599px;top:177px"><h4>Car Donations Help Fund Programs:</h4><p>And benefit National Heroes Support Fund. An IRS 501(c)3 nonprofit organization.</p></div>
  <div class="reason" style="left:102px;top:258px"><h4>Schedule a Free Pickup:</h4><p>Complete the form and a representative will call you to arrange a convenient time to pickup your car.</p></div>
</section>

<footer class="site-footer">
  <div class="social"><span></span><span></span><span></span><span></span><span></span></div>
  <div class="copy">© 2016 Rides for Heroes. All right reserved</div>
</footer>

</body>
</html>
```